I would like a flyer for the ultimate masquarade ball. This will be a PARTY! We need a flyer that will jump out and catch the attention of anyone who sees it. We would like plenty of purple and gold to be used in the flyer. The final design should communicate the ultmate, upscale, classy, exciting masquarade ball ever!

This flyer must be designed for high resolution for printing on 4" x 6" flyers.

Requirements
Must have
• Zeta Kappa Chapter Presents
Lantern Velvet & Ember MasQUErade Ball
1 March 2014
8pm - 1am
3-Course Plated Dinner
Cash Bar
RSVP By: 28 Feb 2014
Halvorsen Gaming & Downs, North Banquet Hall
DJ Tavrik
Details & Tickets: http://lanternvelvetemberball.ticketnook.example
More Info? 555-318-7726
Dress Code: Black Tie & Traditional Dress, Costumes & Masks Preferred

```html
<!DOCTYPE html>
<html lang="en">
<head>
<meta charset="utf-8">
<title>Lantern Velvet &amp; Ember Masquerade Ball</title>
<link rel="stylesheet" href="https://fonts.googleapis.com/css2?family=Cinzel:wght@400;500;600&family=Great+Vibes&display=swap">
<style>
  :root {
    --page: #ffffff;
    --ink-black: #070607;
    --plum-deep: #1e1020;
    --plum: #3a1846;
    --bronze: #3a2214;
    --gold-light: #ecd6ad;
    --gold: #d9bf92;
    --gold-muted: #bba58a;
    --silver: #b9b2b0;
  }
  * { margin: 0; padding: 0; box-sizing: border-box; }
  html, body {
    width: 1200px; height: 970px; overflow: hidden;
    background: var(--page);
  }
  .flyer {
    position: absolute; left: 47px; top: 131px;
    width: 1104px; height: 751px;
    overflow: hidden;
    background: var(--ink-black);
    font-family: "Cinzel", "Times New Roman", serif;
    color: var(--gold-light);
  }
  .stage-photo {
    position: absolute; left: 0; top: 0; width: 1104px; height: 689px;
    background:
      radial-gradient(ellipse 30% 55% at 82% 45%, rgba(90,52,26,.75), rgba(0,0,0,0) 70%),
      radial-gradient(ellipse 45% 60% at 45% 40%, rgba(74,30,92,.8), rgba(0,0,0,0) 72%),
      linear-gradient(180deg, #0b070c 0%, #1c0f22 50%, #120a14 100%);
  }
  .sparkle-field {
    position: absolute; left: 40px; top: 10px; width: 360px; height: 290px;
    background: radial-gradient(ellipse at 45% 40%, rgba(255,255,255,.14), rgba(255,255,255,0) 65%);
  }
  .band { position: absolute; left: 0; top: 0; }
  .block {
    position: absolute; text-align: center; transform: translateX(-50%);
    white-space: nowrap; font-weight: 600;
  }
  .presenter { left: 557px; top: 50px; font-size: 29px; line-height: 34px; letter-spacing: .5px; }
  .presents { left: 555px; top: 90px; font-size: 20px; line-height: 24px; font-weight: 500; color: var(--gold); }
  .details-left { left: 199px; top: 116px; font-size: 19px; line-height: 31px; }
  .details-right { left: 898px; top: 114px; font-size: 19px; line-height: 31px; }
  .details-right .dj { display: block; font-size: 23px; line-height: 32px; font-weight: 500; }
  .mask-art {
    position: absolute; left: 414px; top: 136px; width: 276px; height: 148px;
    border-radius: 48% 48% 40% 40% / 55% 55% 45% 45%;
    background: radial-gradient(ellipse at 50% 45%, #3a2a22, #141010 70%);
    box-shadow: 0 0 0 3px #a88d62 inset;
  }
  .mask-reflection {
    position: absolute; left: 414px; top: 290px; width: 276px; height: 70px;
    background: linear-gradient(180deg, rgba(120,100,80,.3), rgba(0,0,0,0));
    border-radius: 40% 40% 50% 50%;
  }
  .title-top {
    left: 548px; top: 352px; font-size: 37px; line-height: 44px;
    font-weight: 500; color: var(--gold-muted); letter-spacing: .5px;
  }
  .title-top .amp { font-size: 58px; line-height: 44px; vertical-align: -4px; }
  .title-script {
    left: 556px; top: 402px; font-family: "Great Vibes", cursive; font-weight: 400;
    font-size: 54px; line-height: 60px; color: var(--gold-muted);
  }
  .date { left: 550px; top: 474px; font-size: 21px; line-height: 26px; font-weight: 500; color: var(--gold); }
  .tickets-label { left: 563px; top: 567px; font-size: 19px; line-height: 24px; }
  .ticket-link {
    left: 563px; top: 601px; width: 508px; height: 33px;
    border: 1px solid var(--gold); font-size: 15px; line-height: 31px; letter-spacing: .3px;
  }
  .phone { left: 565px; top: 647px; font-size: 19px; line-height: 24px; }
  .dress-code {
    position: absolute; left: 0; right: 0; bottom: 0; height: 62px;
    background: var(--plum-deep);
    text-align: center; line-height: 62px; font-size: 19px; font-weight: 600;
  }
</style>
</head>
<body>
<div class="flyer">
  <div class="stage-photo" role="img" aria-label="Photograph of a purple and bronze stage curtain lit by spotlights"></div>
  <div class="sparkle-field" role="img" aria-label="Scattered glitter sparkles"></div>
  <svg class="band" width="1104" height="751" viewBox="0 0 1104 751" aria-hidden="true">
    <defs>
      <radialGradient id="bandGlow" cx="50%" cy="50%" r="50%">
        <stop offset="0" stop-color="#3a1840" stop-opacity=".7"/>
        <stop offset="1" stop-color="#000" stop-opacity="0"/>
      </radialGradient>
    </defs>
    <path d="M0,229 Q552,329 1104,229 L1104,581 Q552,471 0,581 Z" fill="#0a080b"/>
    <path d="M0,229 Q552,329 1104,229 L1104,581 Q552,471 0,581 Z" fill="url(#bandGlow)"/>
    <path d="M0,229 Q552,329 1104,229" fill="none" stroke="var(--silver)" stroke-width="4"/>
    <path d="M0,581 Q552,471 1104,581" fill="none" stroke="var(--silver)" stroke-width="4"/>
  </svg>

  <div class="block presenter">Zeta Kappa Chapter</div>
  <div class="block presents">Presents</div>

  <div class="block details-left">3-Course Plated Dinner<br>Cash Bar<br>RSVP By: 28 Feb 2014</div>
  <div class="block details-right"><span class="dj">- DJ Tavrik -</span>Halvorsen Gaming &amp; Downs<br>North Banquet Hall</div>

  <div class="mask-art" role="img" aria-label="Ornate black and gold Venetian masquerade mask"></div>
  <div class="mask-reflection" role="img" aria-label="Soft reflection of the mask"></div>

  <div class="block title-top">Lantern Velvet <span class="amp">&amp;</span></div>
  <div class="block title-script">Ember Masquerade Ball</div>
  <div class="block date">1 March 2014 &nbsp;I&nbsp; 8pm - 1am</div>

  <div class="block tickets-label">Details &amp; Tickets:</div>
  <div class="block ticket-link">http://lanternvelvetemberball.ticketnook.example</div>
  <div class="block phone">More Info : 555-318-7726</div>

  <div class="dress-code">Dress Code: Black Tie &amp; Traditional Dress, Costumes &amp; Masks Preferred</div>
</div>
</body>
</html>
```